Stylish High End Wedding Videography/Films Website (BDMR)

We need a modern and high-end website look for our wedding video and films business. We films weddings all over the United Kingdom and at European destinations so need something to reflect our work. The website should be visually stunning with images and videos being the focal point as this is what our services are;

I have uploads of some items I like and the features the site needs to have. These have been taken from other websites using standout features.

We need the following pages;

1 - Homepage
2 - Films Index Page
3 - Individual Films Page
4 - Prices / Collection Page
5 - Reviews
6 - Options
7 - About
8 - Contact
9 - Blog Index
10 - Blog Page

All pages must be consistent so have a similar style.

Pages on menu:
Films
Prices
Reviews
Options
About
Contact

We require a responsive look too. Over 90% of our visitors access the website via their mobile devices.

Please use the colours from our logo to incorporate into the website.

Target Market(s)

Wedding Couples

Industry/Entity Type

Wedding Photography

Number of Pages Required

5+ page

Font styles to use
Sans Serif
Script

Requirements
Must have
• The logo must be in the centre of the menu at the top.

Social icons at the bottom of the page.

Use only two fonts including Lore which is supplied
Nice to have
• Different video for each page on the top header. This will play behind the menu.

```html
<!DOCTYPE html>
<html lang="en">
<head>
<meta charset="utf-8">
<title>BDMR — Wedding Films</title>
<link href="https://fonts.googleapis.com/css2?family=Montserrat:ital,wght@0,300;0,400;0,500;0,600;0,700;1,300&display=swap" rel="stylesheet">
<style>
  :root{
    --gold:#a58e52;
    --gold-light:#c9b27a;
    --ink:#2f2f2f;
    --text:#6b6b6b;
    --grey-band:#f1f1f1;
    --white:#ffffff;
    --footer:#39322d;
    --footer-text:#cfc6b8;
    --badge:#e8dc4a;
    --social:#5b524b;
  }
  *{margin:0;padding:0;box-sizing:border-box}
  html,body{width:1200px;height:3556px;overflow:hidden}
  body{position:relative;background:var(--white);font-family:"Montserrat",sans-serif;color:var(--ink)}
  .abs{position:absolute}

  /* Hero */
  .hero{left:0;top:0;width:1200px;height:460px;
    background:
      radial-gradient(ellipse 180px 260px at 340px 300px,rgba(245,245,242,.55),rgba(245,245,242,0) 70%),
      radial-gradient(ellipse 120px 260px at 440px 260px,rgba(30,32,38,.45),rgba(30,32,38,0) 70%),
      linear-gradient(180deg,#6e7470 0%,#a4aaa5 22%,#b9bdb4 30%,#7f9360 42%,#667e45 65%,#4f6535 85%,#3f5229 100%)}
  .hero-shade{left:0;top:0;width:1200px;height:460px;background:linear-gradient(90deg,rgba(0,0,0,.3),rgba(0,0,0,0) 55%)}
  .nav{left:0;top:62px;width:1200px;height:40px}
  .nav a{position:absolute;top:16px;color:var(--white);font-size:13px;font-weight:500;text-decoration:none;letter-spacing:.5px}
  .nav-line{position:absolute;top:24px;height:1px;background:rgba(255,255,255,.6)}
  .brand{position:absolute;left:520px;top:0;width:160px;text-align:center;color:var(--white);font-size:28px;font-weight:600;letter-spacing:6px}
  .hero-title{left:150px;top:358px;color:var(--white);font-size:46px;font-weight:700;line-height:56px}
  .hero-sub{left:152px;top:420px;color:var(--white);font-size:15px;font-weight:600}

  /* Sections */
  .section-title{left:150px;font-size:26px;font-weight:600;color:var(--ink)}
  .band{left:0;width:1200px;background:var(--grey-band)}
  .photo{box-shadow:0 10px 30px rgba(0,0,0,.12)}
  .lead{left:150px;top:1040px;width:900px;font-size:17px;line-height:26px;color:var(--text);font-weight:400}
  .body-copy{left:150px;width:900px;font-size:11px;line-height:18px;color:var(--text)}
  .read-more{left:550px;top:1444px;font-size:11px;letter-spacing:2px;color:var(--text)}
  .read-more::before{content:"";display:inline-block;width:2px;height:12px;background:var(--gold);margin-right:10px;vertical-align:-2px}

  .dots{left:0;top:2206px;width:1200px;text-align:center;font-size:0}
  .dots span{display:inline-block;width:7px;height:7px;border-radius:50%;background:#d6d6d6;margin:0 3px}
  .dots span.on{background:#8a8a8a}

  .quote{left:250px;top:2820px;width:700px;text-align:center;font-size:17px;line-height:26px;color:var(--text);font-style:italic;font-weight:300}
  .quote .mark{color:var(--gold);font-style:normal}
  .avatar{left:580px;top:2962px;width:40px;height:40px;border-radius:50%;background:linear-gradient(135deg,#8b7b6e,#3d3a3a)}
  .client{left:0;top:3016px;width:1200px;text-align:center;font-size:11px;font-weight:600;color:var(--ink)}

  /* CTA */
  .cta{left:0;top:3100px;width:1200px;height:160px;background:var(--gold);display:flex;align-items:center;justify-content:center;gap:28px}
  .cta h2{font-size:24px;font-weight:600;color:var(--ink);white-space:nowrap}
  .cta .btn{width:124px;height:36px;background:var(--footer);color:var(--footer-text);font-size:10px;line-height:36px;text-align:center;letter-spacing:.5px;white-space:nowrap}

  /* Footer */
  .footer{left:0;top:3260px;width:1200px;height:296px;background:var(--footer)}
  .footer-brand{position:absolute;left:150px;top:56px;font-size:30px;font-weight:600;color:var(--gold);letter-spacing:4px}
  .footer h4{position:absolute;font-size:11px;font-weight:600;letter-spacing:2px;color:var(--white)}
  .footer p{position:absolute;font-size:12px;line-height:18px;color:var(--footer-text);white-space:nowrap}
  .footer .phone{color:var(--gold-light);font-size:15px;font-weight:500}
  .badge{position:absolute;left:986px;top:70px;width:56px;height:56px;border-radius:50%;background:var(--badge)}
  .social{position:absolute;top:174px;width:24px;height:24px;border-radius:50%;background:var(--social)}
  .copyright{position:absolute;left:150px;top:262px;font-size:10px;color:#8f8679}
  .to-top{position:absolute;left:1150px;top:-110px}
</style>
</head>
<body>

<header>
  <div class="abs hero" role="img" aria-label="Photo of a bride and groom walking hand in hand across a green field"></div>
  <div class="abs hero-shade"></div>
  <nav class="abs nav">
    <span class="nav-line" style="left:150px;width:126px"></span>
    <a href="#" style="left:300px">Films</a>
    <a href="#" style="left:370px">Prices</a>
    <a href="#" style="left:442px">Reviews</a>
    <span class="brand">BDMR</span>
    <a href="#" style="left:700px">Options</a>
    <a href="#" style="left:786px">About</a>
    <a href="#" style="left:856px">Contact</a>
    <span class="nav-line" style="left:930px;width:120px"></span>
  </nav>
  <h1 class="abs hero-title">Ella &amp; James</h1>
  <p class="abs hero-sub">The Old Mill, Hartwell</p>
</header>

<main>
  <section>
    <h2 class="abs section-title" style="top:544px">Wedding Films</h2>
    <div class="abs band" style="top:860px;height:720px"></div>
    <div class="abs photo" style="left:272px;top:608px;width:660px;height:344px;background:
      radial-gradient(ellipse 140px 200px at 200px 220px,rgba(250,248,245,.9),rgba(250,248,245,0) 75%),
      radial-gradient(ellipse 150px 220px at 500px 250px,rgba(30,30,36,.85),rgba(30,30,36,0) 75%),
      linear-gradient(135deg,#e6e2dc,#bfb6ab 50%,#8c8178)" role="img" aria-label="Still from the wedding film: the couple laughing together"></div>
    <p class="abs lead">Ella and James's wedding in August 2019 brought us one of the best natural shots of the wedding season when Ella and her father were walking down the aisle at St Anne's church. They turned to each other and smiled which was so emotional and one of the reasons why Vow Stories TV showcased the video on their platform.</p>
    <p class="abs body-copy" style="top:1168px">We were asked by Ella and James to film their wedding following a recommendation from a couple we filmed last year, and we were thrilled to be part of such a relaxed day. Their venue suited our natural style perfectly and gave us plenty of light to work with.</p>
    <p class="abs body-copy" style="top:1222px">The couple chose to have their reception at The Old Mill, set in open countryside, and the grounds gave us a beautiful backdrop for portraits. The speeches were full of laughter and tears, and the evening closed with a first dance under warm festoon lights that we will remember for a long time.</p>
    <p class="abs body-copy" style="top:1276px">Filming a wedding is about capturing the moments that pass too quickly, the glances and the quiet words. We kept our presence light so the day could unfold naturally, and the finished film tells their story just as they lived it.</p>
    <span class="abs read-more">READ MORE</span>
  </section>

  <section>
    <h2 class="abs section-title" style="top:1636px">Unique Photography</h2>
    <div class="abs" style="left:0;top:1712px;width:144px;height:456px;background:linear-gradient(180deg,#e2e2e2 0%,#c4c4c4 40%,#8a8a8a 60%,#5c5c5c 100%)" role="img" aria-label="Black and white photo of a guest in a field"></div>
    <div class="abs" style="left:272px;top:1712px;width:324px;height:456px;background:radial-gradient(ellipse 110px 200px at 170px 280px,rgba(60,60,60,.55),rgba(60,60,60,0) 80%),linear-gradient(180deg,#f2f2f2,#cfcfcf 45%,#8d8d8d)" role="img" aria-label="Black and white photo of bridesmaids getting ready"></div>
    <div class="abs" style="left:608px;top:1712px;width:324px;height:456px;background:radial-gradient(ellipse 100px 220px at 180px 300px,rgba(250,250,250,.8),rgba(250,250,250,0) 80%),linear-gradient(180deg,#ececec,#b4b4b4 50%,#6f6f6f)" role="img" aria-label="Black and white photo of the bride's dress being fastened"></div>
    <div class="abs" style="left:952px;top:1712px;width:248px;height:456px;background:linear-gradient(180deg,#d9d9d9,#b0b0b0 55%,#7a7a7a)" role="img" aria-label="Black and white photo of wedding details"></div>
    <div class="abs dots"><span></span><span class="on"></span><span></span><span></span><span></span><span></span><span></span><span></span></div>
  </section>

  <section>
    <h2 class="abs section-title" style="top:2304px">Client Testimonial</h2>
    <div class="abs band" style="top:2640px;height:400px"></div>
    <div class="abs photo" style="left:272px;top:2392px;width:660px;height:336px;background:radial-gradient(ellipse 120px 190px at 330px 200px,rgba(250,250,250,.6),rgba(250,250,250,0) 80%),linear-gradient(180deg,#e0e0e0,#9c9c9c 50%,#4d4d4d)" role="img" aria-label="Black and white photo of the couple walking up the aisle"></div>
    <p class="abs quote"><span class="mark">“</span> Sed ut perspiciatis unde omnis iste natus error sit voluptatem accusantium doloremque laudantium, totam rem aperiam, eaque ipsa quae ab illo inventore veritatis et quasi architecto beatae vitae dicta sunt explicabo <span class="mark">”</span></p>
    <div class="abs avatar" role="img" aria-label="Portrait of the couple"></div>
    <p class="abs client">Ella &amp; James</p>
  </section>

  <section class="abs cta">
    <h2>Start your project with us</h2>
    <span class="btn">Get Started Now</span>
  </section>
</main>

<footer class="abs footer">
  <svg class="to-top" width="14" height="14" viewBox="0 0 14 14"><path d="M7 12V2M3 6l4-4 4 4" fill="none" stroke="#a58e52" stroke-width="1.5"/></svg>
  <span class="footer-brand">BDMR</span>
  <h4 style="left:340px;top:56px">CONTACT US</h4>
  <p class="phone" style="left:340px;top:86px">Call: +44 7700 900123</p>
  <p style="left:340px;top:108px">E: hello@bdmrfilms.example</p>
  <h4 style="left:670px;top:56px">GET IN TOUCH</h4>
  <p style="left:670px;top:86px;color:var(--white);font-size:14px">HW4 2QL Hartwell</p>
  <p style="left:670px;top:108px;font-size:10px">Brookfield Plain, United Kingdom</p>
  <span class="badge"></span>
  <span class="social" style="left:980px"></span>
  <span class="social" style="left:1010px"></span>
  <span class="social" style="left:1040px"></span>
  <p class="copyright">© 2024 BDMR. All Rights Reserved</p>
</footer>

</body>
</html>
```